Bright Fern Custom Homes business card. Double sided. Modern. professional

Bright Fern Custom Homes
contemporary modern design with our logo /
Double sided with all our contact information
Use same Green colors as in our Logo. Contemporary logo that grabs your attention. Visually pleasing and balanced. Easy to read, and Vibrant. Would love an option for rounded edges. Embossed logo would be amazing.
Contact Information for Business Card
Dana Welk Owner / General Contractor Bright Fern Custom Homes p: 704.552.1830 m: 912.648.2071 e: brightferncustomhomes@mailbox.example w: www.brightferncustomhomes.example 218 Pryor Meadow Lane Batesburg, SC 29041

```html
<!DOCTYPE html>
<html lang="en">
<head>
<meta charset="utf-8">
<title>Bright Fern Custom Homes – Business Card</title>
<link rel="stylesheet" href="https://fonts.googleapis.com/css2?family=Cinzel:wght@400;600&family=Open+Sans:wght@400;700&display=swap">
<style>
  :root {
    --fern-green: #5e7536;
    --fern-green-deep: #4f6429;
    --fern-green-light: #7fa33d;
    --card-white: #ffffff;
    --backdrop: #2b2b2b;
    --text-light: #ffffff;
  }
  * { margin: 0; padding: 0; box-sizing: border-box; }
  html, body { width: 1200px; height: 1015px; overflow: hidden; }
  body {
    background: var(--backdrop);
    font-family: "Open Sans", Arial, sans-serif;
    position: relative;
  }
  .card {
    position: absolute;
    left: 240px;
    width: 720px;
    height: 411px;
    border-radius: 14px;
    overflow: hidden;
  }
  .card--front { top: 70px; background: var(--fern-green); }
  .card--back { top: 534px; background: var(--fern-green); }

  .front-brand {
    position: absolute;
    inset: 0;
    display: flex;
    align-items: center;
    justify-content: center;
    gap: 18px;
  }
  .front-brand__mark {
    width: 58px; height: 58px; border-radius: 50%;
    background: var(--fern-green-deep);
  }
  .front-brand__name {
    font-family: "Cinzel", Georgia, serif;
    font-weight: 400;
    font-size: 40px;
    letter-spacing: 2px;
    color: var(--fern-green-deep);
    line-height: 1.1;
  }

  .back-art { position: absolute; inset: 0; }

  .back-brand {
    position: absolute;
    left: 465px; top: 80px;
    width: 250px;
    text-align: center;
  }
  .back-brand__name {
    font-family: "Cinzel", Georgia, serif;
    font-weight: 400;
    font-size: 28px;
    letter-spacing: 1.5px;
    line-height: 1.15;
    color: var(--fern-green);
  }

  .contact {
    position: absolute;
    left: 48px; top: 52px;
    color: var(--text-light);
  }
  .contact__name {
    font-family: "Cinzel", Georgia, serif;
    font-weight: 600;
    font-size: 30px;
    letter-spacing: 1px;
    line-height: 1;
  }
  .contact__role { font-size: 15px; margin-top: 2px; }
  .contact__address { margin-top: 38px; font-size: 16px; line-height: 1.3; }
  .contact__company { font-weight: 700; }
  .contact__lines { margin-top: 38px; list-style: none; font-size: 16px; line-height: 1.45; }
  .contact__lines li { display: flex; align-items: center; gap: 8px; }
  .contact__icon { width: 15px; height: 15px; flex: none; }
</style>
</head>
<body>

<section class="card card--front" aria-label="Card front">
  <div class="front-brand">
    <span class="front-brand__mark"></span>
    <span class="front-brand__name">Bright Fern<br>Custom Homes</span>
  </div>
</section>

<section class="card card--back" aria-label="Card back">
  <svg class="back-art" width="720" height="411" viewBox="0 0 720 411" aria-hidden="true">
    <circle cx="590" cy="118" r="222" fill="none" stroke="var(--card-white)" stroke-width="3"/>
    <circle cx="600" cy="110" r="210" fill="var(--card-white)"/>
    <path d="M414 42 A198 198 0 0 0 566 305" fill="none" stroke="var(--fern-green-light)" stroke-width="4"/>
  </svg>

  <div class="back-brand">
    <div class="back-brand__name">Bright Fern<br>Custom Homes</div>
  </div>

  <div class="contact">
    <div class="contact__name">DANA WELK</div>
    <div class="contact__role">Owner / General Contractor</div>
    <div class="contact__address">
      <div class="contact__company">Bright Fern Custom Homes</div>
      <div>218 Pryor Meadow Lane</div>
      <div>Batesburg, SC 29041</div>
    </div>
    <ul class="contact__lines">
      <li>
        <svg class="contact__icon" viewBox="0 0 16 16"><path d="M3 1.5l3 .5 1 3-2 1.5a9 9 0 0 0 4.5 4.5L11 9l3 1 .5 3-2 1.5C7 14 2 9 1.5 3.5z" fill="var(--text-light)"/></svg>
        704.552.1830
      </li>
      <li>
        <svg class="contact__icon" viewBox="0 0 16 16"><rect x="4" y="1" width="8" height="14" rx="1.5" fill="none" stroke="var(--text-light)" stroke-width="1.5"/><circle cx="8" cy="12.5" r="0.9" fill="var(--text-light)"/></svg>
        912.648.2071
      </li>
      <li>
        <svg class="contact__icon" viewBox="0 0 16 16"><rect x="1" y="3.5" width="14" height="9" fill="none" stroke="var(--text-light)" stroke-width="1.5"/><path d="M1 3.5l7 5.5 7-5.5" fill="none" stroke="var(--text-light)" stroke-width="1.5"/></svg>
        brightferncustomhomes@mailbox.example
      </li>
      <li>
        <svg class="contact__icon" viewBox="0 0 16 16"><g fill="none" stroke="var(--text-light)" stroke-width="1.3"><circle cx="8" cy="8" r="6.5"/><ellipse cx="8" cy="8" rx="3" ry="6.5"/><path d="M1.5 8h13M2.5 4.8h11M2.5 11.2h11"/></g></svg>
        www.brightferncustomhomes.example
      </li>
    </ul>
  </div>
</section>

</body>
</html>
```